Business Card Re-Design for a Lighting Designer

I would like my business card re-designed. It is currently high gloss and they scratch too easily. I don not think the current design lends itself well to a matte finish. I have included the current design for reference along with our company logo.
Check out our website for current branding.
http://www.brambleorchidstudio.example

Updates
Some of the top contenders are muslim and it is a holiday for them. I do not want to discriminate and would expect the same courtesy for holidays we celebrate.
Target Market(s)
Interior Designers, Architects
Contact Information for Business Card
Logo - Name, Title, Address, Telephone Number and Extension, Email
Font styles to use
Requirements
Must have
- All the information listed on the current business card. If you use Red, it needs to be the red from our logo.
Nice to have
- Vertical and Horizontal Designs will be entertained.
Should not have
- Requirements for a glossy finish...should not look too corporate since we are a design firm.

```html
<!DOCTYPE html>
<html lang="en">
<head>
<meta charset="utf-8">
<title>Bramble Orchid Studio — Business Card</title>
<link rel="stylesheet" href="https://fonts.googleapis.com/css2?family=Didact+Gothic&family=Roboto+Condensed:wght@300&family=Open+Sans:wght@400&display=swap">
<style>
  :root {
    --backdrop: #231f20;
    --card: #ffffff;
    --brand-red: #990000;
    --ink: #111111;
    --muted: #8a8a8a;
    --rule-pink: #c97a7a;
    --facet-light: #f2d4d4;
    --facet-mid: #b81c1c;
    --facet-dark: #1a0000;
  }
  html, body {
    margin: 0;
    padding: 0;
    width: 1200px;
    height: 1200px;
    overflow: hidden;
    background: var(--backdrop);
  }
  .stage {
    position: relative;
    width: 1200px;
    height: 1200px;
  }
  .card {
    position: absolute;
    width: 1090px;
    height: 640px;
    background: var(--card);
    transform: scale(0.6757);
    transform-origin: top left;
    overflow: hidden;
  }
  .card--front { left: 233px; top: 143px; }
  .card--back  { left: 231px; top: 625px; }

  .facets {
    position: absolute;
    inset: 0;
    width: 1090px;
    height: 640px;
  }

  /* Front */
  .front-brand {
    position: absolute;
    left: 222px;
    top: 140px;
    width: 300px;
  }
  .brand-square {
    width: 90px;
    height: 90px;
    background: var(--brand-red);
    margin-bottom: 28px;
  }
  .brand-name {
    font-family: "Roboto Condensed", sans-serif;
    font-weight: 300;
    color: var(--ink);
    font-size: 58px;
    line-height: 56px;
    margin: 0;
    text-transform: uppercase;
  }
  .brand-rule {
    margin-top: 22px;
    width: 280px;
    height: 7px;
    background: var(--rule-pink);
  }
  .brand-tagline {
    margin-top: 10px;
    font-family: "Open Sans", sans-serif;
    font-size: 17px;
    letter-spacing: 1.6px;
    color: var(--muted);
  }

  /* Back */
  .back-brand {
    position: absolute;
    left: 112px;
    top: 200px;
    width: 160px;
    font-family: "Roboto Condensed", sans-serif;
    font-weight: 300;
    font-size: 30px;
    line-height: 29px;
    color: var(--ink);
    text-transform: uppercase;
  }
  .holder {
    position: absolute;
    left: 30px;
    top: 360px;
    width: 322px;
    text-align: center;
    font-family: "Roboto Condensed", sans-serif;
    font-weight: 300;
    font-size: 50px;
    line-height: 60px;
    color: var(--ink);
    letter-spacing: -1px;
  }
  .divider {
    position: absolute;
    left: 370px;
    top: 118px;
    width: 7px;
    height: 403px;
    background: var(--brand-red);
  }
  .veil {
    position: absolute;
    left: 888px;
    top: 140px;
    width: 156px;
    height: 360px;
    background: rgba(255,255,255,0.4);
  }
  .contact {
    position: absolute;
    left: 434px;
    top: 158px;
    width: 610px;
    margin: 0;
    font-family: "Didact Gothic", sans-serif;
    font-style: normal;
    font-size: 36px;
    line-height: 52px;
    letter-spacing: -0.5px;
    white-space: nowrap;
    color: var(--ink);
  }
  .contact .gap { display: block; height: 52px; }
  .website {
    position: absolute;
    left: 0;
    right: 0;
    top: 580px;
    text-align: center;
    font-family: "Didact Gothic", sans-serif;
    font-size: 23px;
    letter-spacing: -0.5px;
    color: var(--ink);
    padding-left: 2px;
  }
</style>
</head>
<body>
<main class="stage">

  <section class="card card--front">
    <svg class="facets" viewBox="0 0 1090 640" role="img" aria-label="Low-poly faceted decoration in red tones fading from pale pink to deep burgundy">
      <defs>
        <linearGradient id="facetFillFront" x1="0.8" y1="0" x2="0.3" y2="1">
          <stop offset="0" stop-color="var(--facet-light)"/>
          <stop offset="0.25" stop-color="#d78a8a"/>
          <stop offset="0.5" stop-color="var(--facet-mid)"/>
          <stop offset="0.75" stop-color="#7a0000"/>
          <stop offset="1" stop-color="var(--facet-dark)"/>
        </linearGradient>
      </defs>
      <polygon fill="url(#facetFillFront)" points="855,0 1090,0 1090,640 745,640 805,573 885,508 870,408 905,343 945,288 935,213 895,158 900,50"/>
    </svg>

    <div class="front-brand">
      <div class="brand-square"></div>
      <h1 class="brand-name">Bramble<br>Orchid Studio</h1>
      <div class="brand-rule"></div>
      <div class="brand-tagline">LIGHTING FOR ARCHITECTURE</div>
    </div>
  </section>

  <section class="card card--back">
    <svg class="facets" viewBox="0 0 1090 640" role="img" aria-label="Low-poly faceted decoration in red tones fading from pale pink to deep burgundy">
      <defs>
        <linearGradient id="facetFillBack" x1="0.8" y1="0" x2="0.3" y2="1">
          <stop offset="0" stop-color="var(--facet-light)"/>
          <stop offset="0.25" stop-color="#d78a8a"/>
          <stop offset="0.5" stop-color="var(--facet-mid)"/>
          <stop offset="0.75" stop-color="#7a0000"/>
          <stop offset="1" stop-color="var(--facet-dark)"/>
        </linearGradient>
      </defs>
      <polygon fill="url(#facetFillBack)" points="855,0 1090,0 1090,640 745,640 805,573 885,508 870,408 905,343 945,288 935,213 895,158 900,50"/>
    </svg>
    <div class="veil"></div>

    <div class="back-brand">Bramble Orchid Studio</div>

    <div class="holder">MAREN HOLT<br>PRINCIPAL</div>

    <div class="divider"></div>

    <address class="contact">
      217 Larkspur Row<br>
      Suite 40<br>
      Fenwick, Oregon 97031 USA<br>
      <span class="gap"></span>
      555.014.2290 x1<br>
      maren@brambleorchidstudio.example
    </address>

    <div class="website">www.brambleorchidstudio.example</div>
  </section>

</main>
</body>
</html>
```